HOME PAGE AND AND SECONDARY DESIGN FOR INTERNAL PAGES

Construction company looking for an easy to navagate professional serious greyscale website with a good clean feel simple clean menu and responsive friendly design. Our main clientele is commercial properties business owners and investors of rental properties. This website is going to be static HTML5 and would need multiple sizing files for clean fast rendering. Clean and accurate design files a must so if your experienced awesome modern greyscale designer let's get started I need this done as soon as possible.

Industry/Entity Type

construction, electrical, plumbing, commercial build outs

Number of Pages Required

2 page

Font styles to use
Sans Serif

Colors

Designer to choose only greyscale colors for use in the design.

Requirements
Must have
• Main Menu... Home, Services, Projects, About our team

```html
<!DOCTYPE html>
<html lang="en">
<head>
<meta charset="utf-8">
<title>Stonebridge Builders</title>
<link rel="stylesheet" href="https://fonts.googleapis.com/css2?family=Roboto:wght@300;400;500;700;900&display=swap">
<style>
:root{
  --bg:#1f1f1f;
  --bg-footer:#151515;
  --white:#ffffff;
  --panel:#f8f8f8;
  --field:#f1f1f1;
  --text-dark:#2a2a2a;
  --muted:#8c8c8c;
  --line:#6a6a6a;
  --accent-red:#c0392b;
}
*{box-sizing:border-box;margin:0;padding:0}
html,body{width:1200px;height:3376px;overflow:hidden}
body{background:var(--bg);font-family:'Roboto',sans-serif;color:var(--white);position:relative}
.abs{position:absolute}
.brand{font-weight:700;font-size:15px;letter-spacing:1px;display:flex;align-items:center;gap:8px;color:var(--white)}
.brand .dot{width:14px;height:14px;background:var(--white);border-radius:50%}
.nav a{position:absolute;top:36px;font-size:11px;letter-spacing:2px;color:var(--white);text-decoration:none;font-weight:400}
.nav .active{border-top:1px solid var(--white);border-bottom:1px solid var(--white);padding:4px 12px}
.hero-title{left:113px;top:362px;font-size:53px;line-height:56px}
.hero-title .light{font-weight:300;display:block}
.hero-title .bold{font-weight:700;display:block}
.square-btn{width:44px;height:44px;background:var(--white);display:flex;align-items:center;justify-content:center}
.btn{background:var(--white);color:var(--text-dark);font-size:10px;letter-spacing:2px;display:flex;align-items:center;justify-content:center;gap:14px;font-weight:500}
.photo{background:linear-gradient(160deg,#cfdfe8,#eef2f4)}
.section-title{left:113px;font-size:53px;font-weight:300;color:#ececec}
.about{left:113px;top:878px;width:974px;height:413px;background:var(--panel)}
.about-title{left:696px;top:898px;font-size:53px;font-weight:300;color:#a5a5a5}
.about-text{left:696px;top:972px;width:332px;font-size:13.5px;line-height:21px;color:var(--text-dark);font-weight:300}
.big-num{font-size:165px;font-weight:900;line-height:1;color:#f1f1f1}
.mission-text{font-size:18.5px;line-height:30px;font-weight:300;color:#f5f5f5}
.tile{overflow:hidden}
.field{left:113px;width:325px;height:37px;background:var(--field);color:#8a8a8a;font-size:12px;padding:11px 17px;letter-spacing:.5px}
.field b{color:var(--accent-red);font-weight:400}
footer{position:absolute;left:0;top:3028px;width:1200px;height:348px;background:var(--bg-footer)}
.f-head{font-size:13px;font-weight:500}
.f-link{font-size:11.5px;font-weight:500}
.f-text{font-size:11px;line-height:21px;font-weight:300;color:#cfcfcf}
.social{width:16px;height:16px;border-radius:50%;background:var(--white)}
</style>
</head>
<body>

<header>
  <div class="abs brand" style="left:115px;top:34px"><span class="dot"></span>STONEBRIDGE<br>BUILDERS</div>
  <nav class="nav">
    <a class="active" style="left:600px;top:32px">MAIN</a>
    <a style="left:706px">SERVICES</a>
    <a style="left:811px">PROJECTS</a>
    <a style="left:921px">ABOUT US</a>
    <a style="left:1020px">OUR TEAM</a>
  </nav>
</header>

<section class="hero">
  <h1 class="abs hero-title"><span class="light">PROJECT</span><span class="bold">Lorum</span></h1>
  <div class="abs square-btn" style="left:113px;top:546px"><svg width="16" height="10"><path d="M16 5H2M6 1 2 5l4 4" stroke="#222" fill="none"/></svg></div>
  <div class="abs square-btn" style="left:175px;top:546px"><svg width="16" height="10"><path d="M0 5h14M10 1l4 4-4 4" stroke="#222" fill="none"/></svg></div>
  <div class="abs" style="left:220px;top:567px;width:225px;height:1px;background:var(--line)"></div>
  <div class="abs" style="left:113px;top:668px;font-size:19px;font-weight:300;line-height:20px">0<br>1</div>
  <svg class="abs" style="left:154px;top:665px" width="28" height="28"><line x1="1" y1="27" x2="27" y2="1" stroke="#fff"/></svg>
  <div class="abs" style="left:207px;top:668px;font-size:19px;font-weight:300">02</div>
  <div class="abs photo" role="img" aria-label="White modern apartment building against a pale blue sky" style="left:445px;top:88px;width:642px;height:689px;background:linear-gradient(135deg,#c4d9e4 0%,#dfe8ec 40%,#f2f2f2 55%,#d9dcde 100%)"></div>
  <div class="abs btn" style="left:445px;top:719px;width:170px;height:54px">VIEW PROJECT <svg width="16" height="10"><path d="M0 5h14M10 1l4 4-4 4" stroke="#222" fill="none"/></svg></div>
</section>

<section>
  <div class="abs about"></div>
  <div class="abs" role="img" aria-label="Glass facade of an office tower" style="left:195px;top:903px;width:225px;height:220px;background:linear-gradient(135deg,#8fb6cc,#d6e6ee)"></div>
  <div class="abs" role="img" aria-label="Black and white angled skyscraper" style="left:195px;top:1149px;width:225px;height:115px;background:linear-gradient(90deg,#111 0%,#666 45%,#f4f4f4 100%)"></div>
  <div class="abs" role="img" aria-label="Blue glass tower corner" style="left:445px;top:928px;width:225px;height:287px;background:linear-gradient(160deg,#e8eef1,#9cc3d6)"></div>
  <h2 class="abs about-title">About</h2>
  <p class="abs about-text">Lorem Ipsum is simply dummy text of the printing and typesetting industry. Lorem Ipsum has been the industry's standard dummy text ever since the 1500s, when an unknown printer took a galley of type and scrambled it to make a type specimen book. It has survived not only five centuries, but also the leap into electronic typesetting, remaining essentially unchanged.</p>
  <div class="abs btn" style="left:696px;top:1157px;width:185px;height:58px">READ MORE <svg width="16" height="10"><path d="M0 5h14M10 1l4 4-4 4" stroke="#222" fill="none"/></svg></div>
</section>

<section>
  <h2 class="abs section-title" style="top:1358px">Main Focus/Mission Statement</h2>
  <div class="abs big-num" style="left:118px;top:1450px">1</div>
  <p class="abs mission-text" style="left:224px;top:1468px;width:260px">Lorem ipsum dolor sit amet, consectetur adipiscing elit. Sed efficitur, lectus et facilisis placerat.</p>
  <div class="abs big-num" style="left:612px;top:1450px">2</div>
  <p class="abs mission-text" style="left:737px;top:1468px;width:345px">Lorem ipsum dolor sit amet, consectetur adipiscing elit. Sed efficitur, lectus et facilisis placerat, magna mauris porttitor tortor, a auctor est felis ut nisl.</p>
</section>

<section>
  <h2 class="abs section-title" style="top:1682px">Our Projects</h2>
  <div class="abs tile" role="img" aria-label="Stadium building rendering, darkened" style="left:113px;top:1791px;width:474px;height:212px;background:linear-gradient(180deg,#4a4c4e,#5c5f60)"></div>
  <div class="abs" style="left:178px;top:1830px;font-size:50px;font-weight:700;line-height:52px">Sample<br>Project</div>
  <div class="abs" style="left:178px;top:1947px;font-size:10px;letter-spacing:2px;display:flex;gap:16px;align-items:center">VIEW MORE <svg width="16" height="10"><path d="M0 5h14M10 1l4 4-4 4" stroke="#fff" fill="none"/></svg></div>
  <div class="abs tile" role="img" aria-label="Dome shaped glass building under blue sky" style="left:612px;top:1791px;width:475px;height:212px;background:linear-gradient(180deg,#2f6fc2 0%,#b9d3c8 55%,#e7dcae 100%)"></div>
  <div class="abs tile" role="img" aria-label="Aerial rendering of an industrial complex" style="left:113px;top:2029px;width:224px;height:211px;background:linear-gradient(135deg,#5e7a4a,#d7c28a 50%,#3f7d7a)"></div>
  <div class="abs tile" role="img" aria-label="Residential apartment blocks" style="left:363px;top:2029px;width:392px;height:211px;background:linear-gradient(180deg,#6a86c8 0%,#e6e8ec 45%,#8c5a4a 85%,#5c7a4e 100%)"></div>
  <div class="abs tile" role="img" aria-label="Monument with red arches" style="left:779px;top:2029px;width:308px;height:211px;background:linear-gradient(180deg,#5d7fc0 0%,#c2cad9 55%,#b0242a 85%,#3a2a2a 100%)"></div>
  <div class="abs btn" style="left:903px;top:2266px;width:184px;height:59px">ALL PROJECTS <svg width="16" height="10"><path d="M0 5h14M10 1l4 4-4 4" stroke="#222" fill="none"/></svg></div>
</section>

<section>
  <h2 class="abs section-title" style="top:2418px">Contact Us</h2>
  <div class="abs field" style="top:2497px">Name</div>
  <div class="abs field" style="top:2543px">Phone Number<b>*</b></div>
  <div class="abs field" style="top:2589px">E-mail<b>*</b></div>
  <div class="abs field" style="top:2636px">Interested In</div>
  <div class="abs field" style="top:2682px;height:121px">Message<b>*</b></div>
  <div class="abs" role="img" aria-label="Man in white shirt talking on a phone, seen from behind" style="left:464px;top:2497px;width:623px;height:306px;background:linear-gradient(90deg,#ffffff 0%,#f3efe8 55%,#c9b49a 80%,#eeeeee 100%)"></div>
  <div class="abs btn" style="left:113px;top:2868px;width:184px;height:59px">SEND EMAIL <svg width="16" height="10"><path d="M0 5h14M10 1l4 4-4 4" stroke="#222" fill="none"/></svg></div>
</section>

<footer>
  <div class="abs brand" style="left:173px;top:50px"><span class="dot"></span>STONEBRIDGE<br>BUILDERS</div>
  <p class="abs f-text" style="left:170px;top:145px;width:410px">Lorem Ipsum is simply dummy text of the printing and typesetting industry. Lorem Ipsum has been the industry's standard dummy text ever since the 1500s, when an unknown printer took a galley of type and scrambled it to make a type specimen book. It has survived not only five centuries, but also the leap into electronic typesetting, remaining essentially unchanged.</p>
  <div class="abs f-head" style="left:648px;top:49px">Information</div>
  <div class="abs f-link" style="left:649px;top:88px">Main</div>
  <div class="abs f-link" style="left:649px;top:119px">Services</div>
  <div class="abs f-link" style="left:649px;top:155px">Projects</div>
  <div class="abs f-link" style="left:649px;top:187px">About us</div>
  <div class="abs f-link" style="left:649px;top:220px">Our Team</div>
  <div class="abs f-head" style="left:863px;top:49px">Social Media</div>
  <span class="abs social" style="left:861px;top:84px"></span>
  <span class="abs social" style="left:905px;top:84px"></span>
  <span class="abs social" style="left:956px;top:84px"></span>
  <span class="abs social" style="left:1003px;top:84px"></span>
  <div class="abs f-head" style="left:859px;top:131px">Contacts</div>
  <svg class="abs" style="left:859px;top:164px" width="12" height="14"><path d="M6 13C2 8 1 6 1 5a5 5 0 0 1 10 0c0 1-1 3-5 8z" stroke="#fff" fill="none"/><circle cx="6" cy="5" r="1.6" stroke="#fff" fill="none"/></svg>
  <div class="abs f-link" style="left:885px;top:168px;line-height:20px">1234 Sample Street<br>Maple Town 00000</div>
  <svg class="abs" style="left:859px;top:219px" width="13" height="13"><path d="M2 1l3 0 1 3-2 1a7 7 0 0 0 4 4l1-2 3 1v3a1 1 0 0 1-1 1A11 11 0 0 1 1 2a1 1 0 0 1 1-1z" stroke="#fff" fill="none"/></svg>
  <div class="abs f-link" style="left:885px;top:220px">555.010.2222</div>
  <svg class="abs" style="left:859px;top:258px" width="14" height="10"><rect x=".5" y=".5" width="13" height="9" stroke="#fff" fill="none"/><path d="M.5 .5 7 6l6.5-5.5" stroke="#fff" fill="none"/></svg>
  <div class="abs f-link" style="left:885px;top:257px">hello@stonebridge.example</div>
  <div class="abs" style="left:0;top:288px;width:1200px;height:1px;background:#2a2a2a"></div>
  <div class="abs" style="left:0;top:308px;width:1200px;text-align:center;font-size:10px;color:#6f6f6f;font-weight:300">© 2023 All Rights Reserved</div>
</footer>

</body>
</html>
```